Flyer for "Learn to Brew Craft Beer" course

NEEDED: A6 flyer designed to advertise my first training course:
Intro to craft beer brewing

The company brand identity was recently bought from Pixel Harbour and it can be seen, with colour scheme on our website: www.TallowMashworks.com.

The flyer is to be in line with my current brand identity and have a strong hook to push people to our site.

The flyer's goal is to get people to visit the site to book on a craft beer brewing training course. The info available to be included, although you have the freedom to include as much or as little as you see fit:

Currently a sale of 60% off on the course cost
RRP £120 Sale Price £50 (limited time only)
Courses will be run in central London
The website is TallowMashworks.com
Hands on, half day course, brunch and a couple of sample beers included
Dates available:
14th December 2014
11th January 2015
18th January 2015
25th January 2015
1st February 2015
8th February 2015
15th February 2015
22nd February 2015

Logo file included, AI version available on request. Any photo on the TallowMashworks.com site is available to be used. Simply pull of the site or I can send to you.

Colour scheme used on site: #FF9700 & #26210D

I will reply to any designs offered between 8pm and 11pm BST each day.

Good luch!

Hi everyone, We have now reviewed the first submissions and there are some ok, some good and a couple of great efforts in there. Here are the following common things that we commented on in our first reviews: 1. WHAT IS THE FLYER TRYING TO SAY... YOU'VE GOT 1 SECOND!!!! This flyer is to be given out in the street. That gives you 1second to tell the reader what the flyer is selling. That is the number 1 priority for the flyer. Please make it your priority as designers. 2. SALE SALE SALE This is the number 2 priority, people love SALES and a big colourful sticker saying SALE or 60% OFF (or both) is to be positioned so once the reader has seen that the flyer is about a craft beer brewing course, they see there is a sale on the course. 3. BRAND PERSONALITY 3rd priority is the Tallow Mashworks brand identity. We picked this name, logo and colour scheme to stand out. Please use these to enhance points 1 & 2, but also get our logo on there is a bold and brash way. 4. USE THE BACK OF THE CARD Place any info that is not required in 1, 2 & 3 on the back, or even remove it all together if YOU feel it is not suited. You are the designer, so make some design decisions! We are happy to ask you to add things back in if we feel it is lacking. Our best guess (and we are NOT designers) is that putting either the dates OR a brief description of the course on the back would be enough info. If you think we can get bother, without overloading the page, give it a go! 5. CALL TO ACTION On the front and on the back, we want a CALL TO ACTION. Book at TallowMashworks.com or just TallowMashworks.com (you do not need http://www before it!!! We live in 2014 not 1994!!!) 6. MAKE IT BOLD, & THEN MAKE IT BOLDER This flyer is to stand out to a person that is handed 1 different leaflet every 2 minutes while walking down a busy London high street. We MUST stand out. Finally, thanks for all the designer so far, your efforts are greatly appreciated and we are very excited about the new revision of the design!

Target Market(s)

City living, young professionals who like to do fun things at the weekend.

Industry/Entity Type

Training

Font styles to use
Sans Serif

Colors
f78f20

Requirements
Must have
• Strong brand identity and call to action
In line with brand identity, see website www.TallowMashworks.com

```html
<!DOCTYPE html>
<html lang="en">
<head>
<meta charset="utf-8">
<title>Learn to Brew Craft Beer – Tallow Mashworks</title>
<link rel="stylesheet" href="https://fonts.googleapis.com/css2?family=Montserrat:wght@400;500;600;700&family=Nothing+You+Could+Do&display=swap">
<style>
  :root {
    --brand-dark: #2a2618;
    --brand-orange: #f78f20;
    --ink-light: #ffffff;
    --ink-dark: #26210d;
    --photo-deep: #1e1208;
    --photo-mid: #6e4116;
    --photo-warm: #b8752a;
    --photo-glow: #e2a449;
  }
  * { margin: 0; padding: 0; box-sizing: border-box; }
  html, body { width: 853px; height: 1200px; overflow: hidden; background: var(--brand-dark); }
  .flyer {
    position: relative;
    width: 853px;
    height: 1200px;
    background: var(--brand-dark);
    font-family: "Montserrat", Arial, sans-serif;
    color: var(--ink-light);
    overflow: hidden;
  }
  .headline {
    position: absolute; top: 50px; left: 0; width: 100%;
    text-align: center; font-size: 29px; font-weight: 500; letter-spacing: 0.3px;
  }
  .limited-tag {
    position: absolute; top: 148px; left: 52px;
    font-family: "Nothing You Could Do", cursive;
    color: var(--brand-orange); font-size: 36px;
    transform: rotate(-8deg); transform-origin: left bottom;
  }
  .sale-ribbon { position: absolute; top: 200px; left: 124px; width: 600px; height: 108px; }
  .sale-text {
    position: absolute; top: 200px; left: 124px; width: 600px; height: 108px;
    display: flex; align-items: center; justify-content: center;
    font-weight: 500;
  }
  .sale-figure { font-size: 62px; font-weight: 500; line-height: 1; position: relative; }
  .sale-figure sup { font-size: 24px; position: absolute; top: -2px; right: -22px; }
  .sale-label { font-size: 31px; margin-left: 24px; }
  .course-summary {
    position: absolute; top: 338px; left: 0; width: 100%;
    text-align: center; font-size: 28px; line-height: 1.32;
  }
  .dates-heading {
    position: absolute; top: 453px; left: 0; width: 100%;
    text-align: center; color: var(--brand-orange); font-size: 20px; font-weight: 500;
  }
  .dates-list {
    position: absolute; top: 492px; left: 0; width: 100%;
    text-align: center; font-size: 18px; white-space: nowrap;
  }
  .dates-list sup { font-size: 11px; }
  .dates-list .sep { color: var(--brand-orange); margin: 0 4px; }
  .info-prompt {
    position: absolute; top: 559px; left: 0; width: 100%;
    text-align: center; font-size: 23px;
  }
  .site-link {
    position: absolute; top: 601px; left: 215px; width: 419px; height: 53px;
    background: var(--brand-orange); color: var(--ink-dark);
    display: flex; align-items: center; justify-content: center;
    font-size: 25px; font-weight: 700;
  }
  .photo-area {
    position: absolute; top: 690px; left: 0; width: 853px; height: 510px;
    background:
      radial-gradient(ellipse 620px 460px at 300px 260px,
        var(--photo-glow) 0%, var(--photo-warm) 30%, var(--photo-mid) 62%, var(--photo-deep) 100%);
  }
  .chevron { position: absolute; top: 0; left: 0; width: 853px; height: 1200px; pointer-events: none; }
  .brand-mark {
    position: absolute; top: 1010px; left: 655px; width: 180px;
    display: flex; flex-direction: column; align-items: center; gap: 12px;
  }
  .brand-dot {
    width: 46px; height: 46px; border-radius: 50%;
    background: var(--ink-light);
  }
  .brand-name {
    text-align: center; font-size: 25px; font-weight: 700; line-height: 1.15;
    color: var(--ink-light); text-transform: uppercase; letter-spacing: 0.5px;
  }
  .location-bar {
    position: absolute; bottom: 0; left: 0; width: 100%; height: 58px;
    background: rgba(20, 16, 8, 0.55);
    display: flex; align-items: center; padding-left: 22px;
    font-size: 24px;
  }
  .location-bar strong { font-weight: 600; margin-right: 8px; }
</style>
</head>
<body>
<main class="flyer">
  <h1 class="headline">LEARN TO BREW CRAFT BEER for only £50</h1>

  <div class="photo-area" role="img" aria-label="Two glasses of frothy golden craft beer in front of a wooden barrel"></div>

  <svg class="chevron" viewBox="0 0 853 1200" aria-hidden="true">
    <polygon points="0,680 853,680 853,748 427,697 0,748" fill="var(--brand-dark)"/>
    <polygon points="0,748 427,697 853,748 853,770 427,719 0,770" fill="var(--brand-orange)"/>
  </svg>

  <p class="limited-tag">limited time only</p>

  <svg class="sale-ribbon" viewBox="0 0 600 108" aria-hidden="true">
    <polygon points="0,0 600,0 572,54 600,108 0,108 28,54" fill="var(--brand-orange)"/>
    <polygon points="22,8 578,8 556,54 578,100 22,100 44,54" fill="none" stroke="var(--brand-dark)" stroke-width="2.5"/>
  </svg>
  <div class="sale-text">
    <span class="sale-figure">60<sup>%</sup></span>
    <span class="sale-label">off on the course cost</span>
  </div>

  <p class="course-summary">Hands on, half day course, brunch and<br>a couple of sample beers included</p>

  <h2 class="dates-heading">Available Dates</h2>
  <p class="dates-list">14<sup>th</sup> Dec<span class="sep">|</span>11<sup>th</sup> Jan<span class="sep">|</span>18<sup>th</sup> Jan<span class="sep">|</span>25<sup>th</sup> Jan<span class="sep">|</span>1<sup>st</sup> Feb<span class="sep">|</span>8<sup>th</sup> Feb<span class="sep">|</span>15<sup>th</sup> Feb<span class="sep">|</span>22<sup>nd</sup> Feb</p>

  <p class="info-prompt">For more information please visit</p>
  <div class="site-link">www.tallowmashworks.com</div>

  <div class="brand-mark">
    <span class="brand-dot" aria-hidden="true"></span>
    <span class="brand-name">Tallow<br>Mashworks</span>
  </div>

  <footer class="location-bar"><strong>LOCATION:</strong> Copperfields, 22-24 Varden St, London</footer>
</main>
</body>
</html>
```